Car Loan Landing Page Redesign

We are looking for a fresh, eye catching and professional redesign of our landing page as attached.
This current template doesn't stand out and doesn't highlight the main part of the page which is the application box.
Our corporate colors are pink #ee245f, black #000, #232323 and colors as in our website www.brindle.com.au
Brindle is Australia's leading car finance brokerage institution and this landing page is geared towards car finance.
We also believe the background banner needs some sort of creative approach.
We also feel that the form steps (once you click on start to compare) needs to be refreshed as well in terms of its form input fields design.
We like to have this whole page redesigned and freshen up so it gives an unique design experience to the users.
Feel free to use your imagination with some great eye catchy banner, and move the elements around as you need to.
Target Market(s)
Australians who are looking for car finance
Industry/Entity Type
Finance
Number of Pages Required
1 page
Font styles to use
Other font styles liked:
- Roboto
Look and feel
Each slider illustrates characteristics of the customer's brand and the style your logo design should communicate.

```html
<!DOCTYPE html>
<html lang="en">
<head>
<meta charset="utf-8">
<title>Brindle – Car Loan Comparison</title>
<link rel="stylesheet" href="https://fonts.googleapis.com/css2?family=Lato:wght@300;400;700&family=Roboto:wght@300;400;500&display=swap">
<style>
:root{
  --pink:#ee245f;
  --pink-dark:#c81c4e;
  --black:#000;
  --charcoal:#232323;
  --slate:#4a4a4a;
  --slate-dark:#3c3c3c;
  --light:#f4f4f4;
  --white:#fff;
  --text:#333;
  --muted:#777;
}
*{margin:0;padding:0;box-sizing:border-box}
html,body{width:1200px;height:3072px;overflow:hidden}
body{font-family:"Lato",Arial,sans-serif;color:var(--text);background:var(--white);position:relative}
.abs{position:absolute}

/* Hero */
.hero{position:absolute;left:0;top:0;width:1200px;height:666px;overflow:hidden}
.hero-photo{position:absolute;inset:0;background:linear-gradient(180deg,#5b6670 0%,#7e8a8f 30%,#3d5a7e 55%,#6b5844 80%,#4a3c30 100%)}
.hero-shade{position:absolute;inset:0;background:rgba(0,0,0,.28)}
.topbar{position:absolute;left:0;top:0;width:1200px;height:123px;background:rgba(20,20,20,.55);border-bottom:1px solid rgba(255,255,255,.2)}
.brand{position:absolute;left:98px;top:18px;color:var(--white);font-family:"Lato",sans-serif;font-weight:300;font-size:72px;line-height:1;letter-spacing:1px}
.brand-tag{position:absolute;left:108px;top:88px;color:var(--white);font-size:15px;letter-spacing:2px;font-weight:400}
.call{position:absolute;left:932px;top:26px;display:flex;align-items:center;gap:12px;color:var(--white)}
.call-icon{width:40px;height:40px;border-radius:50%;border:2px solid var(--pink);display:flex;align-items:center;justify-content:center}
.call-label{font-size:13px;display:block}
.call-number{font-size:21px;font-weight:400;display:block}
.tagline{position:absolute;right:104px;top:84px;color:var(--white);font-style:italic;font-size:17px}
.hero-title{position:absolute;left:0;width:1200px;top:186px;text-align:center;color:var(--white);font-weight:300;font-size:45px}
.hero-sub{position:absolute;left:0;width:1200px;top:244px;text-align:center;color:var(--white);font-weight:300;font-size:32px}
.step{position:absolute;top:336px;width:260px;text-align:center;color:var(--white)}
.step-circle{width:184px;height:184px;margin:0 auto;border-radius:50%;background:var(--pink);border:6px solid rgba(255,255,255,.35);display:flex;align-items:center;justify-content:center;position:relative}
.step-badge{position:absolute;left:50%;bottom:-26px;transform:translateX(-50%);width:60px;height:60px;border-radius:50%;background:var(--white);color:var(--charcoal);font-size:10px;line-height:1;display:flex;flex-direction:column;align-items:center;justify-content:center}
.step-badge b{font-size:20px;font-weight:700}
.step-text{margin-top:38px;font-size:19px;line-height:1.35}
.step-arrow{position:absolute;top:408px}
.hero-notch{position:absolute;left:232px;top:638px;width:0;height:0;border-left:28px solid transparent;border-right:28px solid transparent;border-bottom:28px solid var(--slate)}

/* Borrow */
.borrow{position:absolute;left:0;top:666px;width:1200px;height:502px;background:linear-gradient(135deg,var(--slate) 0%,var(--slate-dark) 100%)}
.borrow-title{position:absolute;left:0;width:1200px;top:74px;text-align:center;color:var(--white);font-weight:300;font-size:42px}
.amount{position:absolute;left:408px;top:164px;width:385px;height:66px;background:var(--white);border-radius:4px;color:var(--pink);font-size:42px;font-weight:300;text-align:center;line-height:66px}
.amount::after{content:"";position:absolute;left:50%;bottom:-12px;margin-left:-12px;border-left:12px solid transparent;border-right:12px solid transparent;border-top:12px solid var(--white)}
.track{position:absolute;left:117px;top:268px;width:973px;height:8px;border-radius:4px;background:#cfcfcf}
.track-fill{position:absolute;left:0;top:0;width:243px;height:8px;border-radius:4px;background:var(--pink)}
.thumb{position:absolute;left:340px;top:254px;width:38px;height:38px;border-radius:50%;background:var(--white);border:6px solid var(--pink)}
.ticks{position:absolute;left:98px;top:298px;width:1012px;display:flex;justify-content:space-between;color:var(--white);font-size:13px;font-weight:700}
.btn-pink{position:absolute;left:408px;top:354px;width:385px;height:66px;border-radius:33px;background:var(--pink);color:var(--white);font-size:25px;font-weight:400;display:flex;align-items:center;justify-content:center;gap:10px;letter-spacing:.5px}

/* Lenders */
.lenders{position:absolute;left:0;top:1168px;width:1200px;height:323px;background:var(--white)}
.lenders-title{position:absolute;left:0;width:1200px;top:60px;text-align:center;font-weight:300;font-size:34px;color:var(--charcoal)}
.lenders-sub{position:absolute;left:0;width:1200px;top:118px;text-align:center;font-size:17px;color:var(--muted)}
.lender-row{position:absolute;left:98px;top:180px;display:flex;gap:11px}
.lender{width:164px;height:77px;border:1px solid #ddd;border-radius:4px;display:flex;align-items:center;justify-content:center;font-size:24px;font-weight:700;color:var(--charcoal)}
.carousel-arrow{position:absolute;top:198px}

/* Features */
.features{position:absolute;left:0;top:1491px;width:1200px;height:403px;background:linear-gradient(135deg,var(--slate) 0%,var(--slate-dark) 100%)}
.feature{position:absolute;width:320px;display:flex;gap:18px;color:var(--white)}
.feature-icon{flex:0 0 82px;height:82px;background:var(--pink);display:flex;align-items:center;justify-content:center}
.feature h3{font-weight:300;font-size:20px;margin-bottom:6px}
.feature p{font-size:13px;line-height:1.45;color:#ddd}

/* How */
.how{position:absolute;left:0;top:1894px;width:1200px;height:768px;overflow:hidden}
.how-photo{position:absolute;inset:0;background:linear-gradient(90deg,#3e4a52 0%,#5a6a70 35%,#7a3030 60%,#b8202a 78%,#5a1a1a 100%)}
.how-shade{position:absolute;inset:0;background:linear-gradient(90deg,rgba(0,0,0,.55) 0%,rgba(0,0,0,.25) 55%,rgba(0,0,0,0) 100%)}
.how-title{position:absolute;left:102px;top:78px;color:var(--white);font-weight:300;font-size:33px;line-height:1.3}
.how-list{position:absolute;left:98px;top:186px;list-style:none}
.how-item{display:flex;align-items:center;width:520px;height:62px;margin-bottom:14px;background:linear-gradient(90deg,rgba(0,0,0,.45),rgba(0,0,0,0))}
.how-icon{flex:0 0 74px;height:62px;background:var(--pink);clip-path:polygon(0 0,85% 0,100% 50%,85% 100%,0 100%);display:flex;align-items:center;justify-content:center;padding-right:10px}
.how-item p{color:var(--white);font-size:14px;line-height:1.5;padding-left:16px}

/* CTA */
.cta{position:absolute;left:0;top:2662px;width:1200px;height:215px;background:var(--pink)}
.cta-title{position:absolute;left:0;width:1200px;top:60px;text-align:center;color:var(--white);font-weight:300;font-size:36px}
.btn-white{position:absolute;left:432px;top:111px;width:336px;height:56px;border-radius:28px;background:var(--white);color:var(--charcoal);font-size:19px;font-weight:700;display:flex;align-items:center;justify-content:center;gap:10px}

/* Footer */
.footer{position:absolute;left:0;top:2877px;width:1200px;height:195px;background:var(--black);color:var(--white)}
.legal{position:absolute;left:98px;top:52px;font-size:13px;line-height:1.7}
.social{position:absolute;left:98px;top:122px;display:flex;gap:18px;font-size:14px;font-family:"Roboto",sans-serif}
.badges{position:absolute;left:716px;top:44px;display:flex;gap:40px;align-items:center}
.badge-a{width:48px;height:78px;background:#f2c400;border-radius:6px}
.badge-b{width:150px;height:40px;border-radius:20px;background:#2a3a5a}
.badge-c{width:140px;height:50px;border-radius:25px;background:#1f4b66}
</style>
</head>
<body>

<header class="hero">
  <div class="hero-photo" role="img" aria-label="Blue sports sedan on an open road with fields and a cloudy sky"></div>
  <div class="hero-shade"></div>
  <div class="topbar">
    <div class="brand">brindle</div>
    <div class="brand-tag">finance · insurance</div>
    <div class="call">
      <span class="call-icon">
        <svg width="20" height="20" viewBox="0 0 24 24"><path fill="#ee245f" d="M6.6 10.8a15.1 15.1 0 0 0 6.6 6.6l2.2-2.2c.3-.3.7-.4 1-.2 1.1.4 2.3.6 3.6.6.6 0 1 .4 1 1V20c0 .6-.4 1-1 1A17 17 0 0 1 3 4c0-.6.4-1 1-1h3.5c.6 0 1 .4 1 1 0 1.3.2 2.5.6 3.6.1.3 0 .7-.2 1z"/></svg>
      </span>
      <span><span class="call-label">Call Us Today</span><span class="call-number">1300 555 019</span></span>
    </div>
    <div class="tagline">Brindle Has Helped Over 35,000 Australians With Their Finance!</div>
  </div>

  <h1 class="hero-title">How Much Can You Save On Your Car Loan?</h1>
  <p class="hero-sub">Comparing car loan lenders could save you thousands!</p>

  <div class="step" style="left:142px">
    <div class="step-circle">
      <svg width="80" height="90" viewBox="0 0 40 46" fill="none" stroke="#fff" stroke-width="2.5"><rect x="4" y="5" width="32" height="38" rx="3"/><rect x="13" y="2" width="14" height="6" rx="2" fill="#ee245f"/><path d="M10 18l3 3 5-5M10 28l3 3 5-5M22 19h8M22 29h8M10 37h20"/></svg>
      <div class="step-badge">STEP<b>01</b></div>
    </div>
    <p class="step-text">Tell Us How Much You<br>Need For Your Next Car!</p>
  </div>
  <div class="step" style="left:470px">
    <div class="step-circle">
      <span style="color:#fff;font-size:96px;font-weight:700;line-height:1">%</span>
      <div class="step-badge">STEP<b>02</b></div>
    </div>
    <p class="step-text">We Provide Lightning Quick<br>Quotes From Our Lenders</p>
  </div>
  <div class="step" style="left:796px">
    <div class="step-circle">
      <svg width="100" height="70" viewBox="0 0 50 34"><path fill="#fff" d="M10 4c1-2 3-3 5-3h20c2 0 4 1 5 3l4 9c3 1 5 3 5 6v9h-6v4h-6v-4H13v4H7v-4H1v-9c0-3 2-5 5-6zm3 9h24l-3-7H16zM8 19a3 3 0 1 0 0 6 3 3 0 0 0 0-6zm34 0a3 3 0 1 0 0 6 3 3 0 0 0 0-6z"/></svg>
      <div class="step-badge">STEP<b>03</b></div>
    </div>
    <p class="step-text">Gain Approval And Drive<br>Away With A Better Deal!</p>
  </div>
  <svg class="step-arrow" style="left:368px" width="110" height="40" viewBox="0 0 110 40"><path d="M4 30 Q55 0 100 22" fill="none" stroke="#fff" stroke-width="3"/><path d="M92 12l12 11-15 5z" fill="#fff"/></svg>
  <svg class="step-arrow" style="left:706px" width="110" height="40" viewBox="0 0 110 40"><path d="M4 30 Q55 0 100 22" fill="none" stroke="#fff" stroke-width="3"/><path d="M92 12l12 11-15 5z" fill="#fff"/></svg>
  <div class="hero-notch"></div>
</header>

<section class="borrow">
  <h2 class="borrow-title">How Much Do You Like To Borrow?</h2>
  <div class="amount">$ 38000</div>
  <div class="track"><div class="track-fill"></div></div>
  <div class="thumb"></div>
  <div class="ticks"><span>$ 5K</span><span>$ 15K</span><span>$ 25K</span><span>$ 35K</span><span>$ 45K</span><span>$ 55K</span><span>$ 65K</span><span>$ 75K</span><span>$ 85K</span><span>$ 95K</span><span>$ 105K</span><span>$ 115K</span><span>$ 125K</span><span>$ 135K</span><span>$ 145K</span></div>
  <div class="btn-pink">START TO COMPARE <span>»</span></div>
</section>

<section class="lenders">
  <h2 class="lenders-title">Compare Multiple Lenders &amp; Save On Your Finance. Get Brindle</h2>
  <p class="lenders-sub">Comparing lenders can help you get great rates and save thousands! Compare Australia's top lenders with Brindle and save.</p>
  <svg class="carousel-arrow" style="left:50px" width="24" height="40" viewBox="0 0 24 40"><path d="M20 2 4 20l16 18" fill="none" stroke="#999" stroke-width="3"/></svg>
  <div class="lender-row">
    <div class="lender">Coinleaf</div>
    <div class="lender">Drivewell</div>
    <div class="lender" style="font-size:20px">Harbour Bank</div>
    <div class="lender" style="font-size:21px">Southcrest</div>
    <div class="lender">Quill</div>
    <div class="lender">Ardena</div>
  </div>
  <svg class="carousel-arrow" style="left:1126px" width="24" height="40" viewBox="0 0 24 40"><path d="M4 2l16 18L4 38" fill="none" stroke="#999" stroke-width="3"/></svg>
</section>

<section class="features">
  <div class="feature" style="left:98px;top:72px">
    <div class="feature-icon"><svg width="50" height="40" viewBox="0 0 50 40" fill="#fff"><circle cx="25" cy="9" r="6"/><circle cx="10" cy="13" r="5"/><circle cx="40" cy="13" r="5"/><path d="M15 34c0-8 4-14 10-14s10 6 10 14zM2 34c0-7 3-11 8-11 3 0 5 1 6 3-2 2-3 5-3 8zM48 34c0-7-3-11-8-11-3 0-5 1-6 3 2 2 3 5 3 8z"/></svg></div>
    <div><h3>Reputable Lenders</h3><p>Brindle is an accredited NBFA member and represents 25+ reputable lenders nationally.</p></div>
  </div>
  <div class="feature" style="left:442px;top:72px">
    <div class="feature-icon"><svg width="46" height="46" viewBox="0 0 46 46" fill="none" stroke="#fff" stroke-width="2.5"><circle cx="15" cy="15" r="10"/><circle cx="31" cy="26" r="10"/><path d="M4 40h38"/></svg></div>
    <div><h3>Compare &amp; Save</h3><p>Compare and save with Brindle. Brindle will shop your deal around from multiple lenders to get you the best deal.</p></div>
  </div>
  <div class="feature" style="left:788px;top:72px">
    <div class="feature-icon"><span style="color:#fff;font-size:46px;font-weight:700">%</span></div>
    <div><h3>Low Interest Rates</h3><p>Brindle, through its lending panel can provide you with some of the lowest rates on the market.</p></div>
  </div>
  <div class="feature" style="left:98px;top:213px">
    <div class="feature-icon"><svg width="46" height="46" viewBox="0 0 46 46" fill="none" stroke="#fff" stroke-width="2.5"><rect x="4" y="6" width="28" height="32" rx="2"/><path d="M10 14h16M10 21h10"/><circle cx="32" cy="32" r="10"/><path d="M32 26v6l4 3"/></svg></div>
    <div><h3>Same Day Approvals</h3><p>Our application process is quick &amp; easy. Brindle has the systems, technology and consultants that can get your application approved fast.</p></div>
  </div>
  <div class="feature" style="left:442px;top:213px">
    <div class="feature-icon"><svg width="46" height="46" viewBox="0 0 46 46" fill="#fff"><path d="M17 4h12l-3 7h-6z"/><path d="M14 13h18c6 6 9 13 9 19 0 6-5 10-18 10S5 38 5 32c0-6 3-13 9-19z"/></svg></div>
    <div><h3>100% Finance</h3><p>100% finance is available to approved customers as the car is almost always sufficient security.</p></div>
  </div>
  <div class="feature" style="left:788px;top:213px">
    <div class="feature-icon"><svg width="44" height="40" viewBox="0 0 44 40" fill="#fff"><path d="M22 38 4 20A10 10 0 0 1 22 6a10 10 0 0 1 18 14z"/></svg></div>
    <div><h3>No Obligation</h3><p>All applications with Brindle are obligation free.</p></div>
  </div>
</section>

<section class="how">
  <div class="how-photo" role="img" aria-label="Red sports car in close-up speeding along a road with motion blur"></div>
  <div class="how-shade"></div>
  <h2 class="how-title">How Brindle Will Help You Find A Great<br>Deal On Your Car Finance</h2>
  <ul class="how-list">
    <li class="how-item"><span class="how-icon"><svg width="30" height="30" viewBox="0 0 30 30" fill="none" stroke="#fff" stroke-width="2"><rect x="3" y="4" width="24" height="22" rx="2"/><path d="M8 11h14M8 16h14M8 21h8"/></svg></span><p>Understand your needs and requirements and find a tailored<br>loan solution based on your financial goals.</p></li>
    <li class="how-item"><span class="how-icon"><svg width="30" height="30" viewBox="0 0 30 30" fill="none" stroke="#fff" stroke-width="2"><rect x="5" y="2" width="20" height="26" rx="2"/><path d="M9 7h12M9 13h2M14 13h2M19 13h2M9 18h2M14 18h2M19 18h2M9 23h2M14 23h2M19 23h2"/></svg></span><p>Ascertain your borrowing power, your capacity for repayments so<br>you always get a loan that's within you budget.</p></li>
    <li class="how-item"><span class="how-icon"><svg width="30" height="30" viewBox="0 0 30 30" fill="none" stroke="#fff" stroke-width="2"><rect x="3" y="3" width="14" height="18" rx="1"/><rect x="13" y="9" width="14" height="18" rx="1"/></svg></span><p>Compare your car loan with 25+ lenders and banks so you gain<br>the best deal from a top lender.</p></li>
    <li class="how-item"><span class="how-icon"><svg width="30" height="30" viewBox="0 0 30 30" fill="none" stroke="#fff" stroke-width="2"><rect x="3" y="4" width="24" height="16" rx="1"/><path d="M9 26l6-6 6 6M8 14l5-4 4 3 5-5"/></svg></span><p>Explain all fees, charges and obligations up front so you know<br>exactly what you're getting when it comes to your car loan.</p></li>
    <li class="how-item"><span class="how-icon"><svg width="30" height="30" viewBox="0 0 30 30" fill="#fff"><circle cx="15" cy="9" r="6"/><path d="M4 28c0-8 5-12 11-12s11 4 11 12z"/></svg></span><p>Provide you with a dedicated personal consultant to manage you<br>application and delivery - every step of the way.</p></li>
    <li class="how-item"><span class="how-icon"><svg width="30" height="30" viewBox="0 0 30 30" fill="none" stroke="#fff" stroke-width="2"><circle cx="15" cy="12" r="6"/><path d="M6 13a9 9 0 0 1 18 0M5 28c1-6 5-9 10-9s9 3 10 9"/></svg></span><p>Provide you with the highest level of customer service and<br>support throughout the life of your loan.</p></li>
  </ul>
</section>

<section class="cta">
  <h2 class="cta-title">Compare Australia's Top Lenders With Us Today. Get Brindle</h2>
  <div class="btn-white">COMPARE CAR LOANS <span style="color:#999">»</span></div>
</section>

<footer class="footer">
  <p class="legal">Copyright © 2016 All rights reserved. Quorra Brindle Pty Ltd - ABN: 00 000 000 000,<br>Australian Credit Licence: 000000. Free Phone: 1300 555 019.</p>
  <div class="social"><span>Linkup</span><span>Reelhub</span><span>Chirp</span><span>Worknet</span><span>Circlr</span><span>Pinboard</span></div>
  <div class="badges">
    <div class="badge-a"></div>
    <div class="badge-b"></div>
    <div class="badge-c"></div>
  </div>
</footer>

</body>
</html>
```